Construction Company Website Design

I need a Website Design for a Construction Company. I have attached logo and business card design files (a.i) to match styles and text for the website. I will need design for 3 pages:
1. A Home page
2. A secondary page (will be different information pages)
3. A contact page with submision form
Website to look professional and match the 'theme' across all pages, using main colours / reverse colours as per design files. Must be clear it is a construction related website without being over the top. Happy for the construction related details (whether that be images/outlines/backgrounds etc to be fairly subtle and not overbearing on the contect of the pages. It will be the content that will be most important, not the images within.

Content has not yet been fully completed but attached is a site map. Each page will need a space for the insertion of the relevant heading and associated content for that particular page. Example can be used as per attached map. If it is preferable to have content completed for this to be a more succesful project please advise and I will complete and submit.

Target Market(s)

Clients for potential construction projects. These could be a range of people. All would be very professional, well educated and put a substantial expection on the quality of website provided.

Industry/Entity Type

Construction

Number of Pages Required

3 page

Font styles to use
Serif
Sans Serif
Other font styles liked:
• fonts preferable as per design files provided unless designer beleives a different font would suit better

Requirements
Must have
• Colour scheme to match logo and business card files provided. Fonts that match as per provided files. Pages must be consistent with the theme carrying across all pages. All pages must have contact details at the bottom of the page.
• Contents of page 1 - 'Home page': multiple tab options / logo link
• Contents of page 2 - 'Secondary page': Top and side navigation / area for information and/or images.
• Contents of page - 'Contact us page': Top and side navigation / Submission form / area for logos such as linkdin, facebook etc.
Nice to have
• Would be good to have a or some generic construction related images - outlines / shadows / effects etc. These might be background images or outlines related to the relevant industry and are consistent across the pages. Could be outlines of buildings, images of men with hardhats etc etc. Good to see colour scheme as per design files used
Should not have
• No pictures of houses. Generally no photos. If any imagery of people must not show faces/details.

```html
<!DOCTYPE html>
<html lang="en">
<head>
<meta charset="utf-8">
<title>Halden Constructions — Quality Construction</title>
<link href="https://fonts.googleapis.com/css2?family=Montserrat:wght@400;500&family=Roboto:wght@500;700&display=swap" rel="stylesheet">
<style>
  :root {
    --sky: #00c6fb;
    --sky-mid: #14a6f0;
    --royal: #2f78dd;
    --white: #ffffff;
    --white-soft: rgba(255,255,255,0.75);
    --line-faint: rgba(255,255,255,0.14);
    --panel: #35475f;
    --photo-warm: #c9822f;
    --photo-cool: #6d8197;
    --photo-vest: #e6492b;
    --page: #ffffff;
  }
  * { box-sizing: border-box; margin: 0; padding: 0; }
  html, body { width: 1200px; height: 745px; overflow: hidden; background: var(--page); }
  body { font-family: "Montserrat", Arial, sans-serif; color: var(--white); }

  .site { position: relative; width: 1200px; height: 745px; background: var(--page); overflow: hidden; }

  .hero {
    position: absolute; left: 0; top: 0; width: 1200px; height: 620px;
    background: linear-gradient(100deg, var(--sky) 0%, var(--sky-mid) 50%, var(--royal) 100%);
  }
  .grid-line { position: absolute; top: 0; width: 1px; height: 620px; background: var(--line-faint); }
  .grid-line.main { background: rgba(255,255,255,0.6); height: 62px; }

  .brand {
    position: absolute; left: 25px; top: 53px;
    font-size: 15px; font-weight: 400; letter-spacing: 2.4px; text-transform: uppercase;
    color: var(--white); white-space: nowrap;
  }

  .main-nav { position: absolute; top: 56px; left: 0; }
  .main-nav a {
    position: absolute; top: 0; white-space: nowrap;
    font-size: 10px; font-weight: 500; letter-spacing: 0.5px; text-transform: uppercase;
    color: var(--white); text-decoration: none;
  }
  .main-nav a::before {
    content: ""; position: absolute; left: -15px; top: 2px;
    width: 6px; height: 6px; border-radius: 50%; border: 1px solid var(--white-soft);
  }
  .main-nav a.active::before { background: var(--white); border-color: var(--white); }

  .social-link {
    position: absolute; top: 47px; width: 30px; height: 30px; border-radius: 50%;
    border: 1px solid var(--white-soft);
    display: flex; align-items: center; justify-content: center;
  }
  .social-link::after {
    content: ""; width: 8px; height: 8px; border-radius: 50%; background: var(--white);
  }

  .hero-title {
    position: absolute; left: 0; top: 190px; width: 1200px; text-align: center;
    font-family: "Roboto", Arial, sans-serif; font-weight: 500; font-size: 64px; letter-spacing: -0.5px;
  }
  .hero-services {
    position: absolute; left: 0; top: 280px; width: 1204px; text-align: center;
    font-size: 12.5px; font-weight: 500; letter-spacing: 4.8px; text-transform: uppercase;
    white-space: nowrap;
  }
  .scroll-cue { position: absolute; left: 584px; top: 332px; }
  .section-dots { position: absolute; left: 1180px; top: 230px; }

  .intro-card {
    position: absolute; left: 185px; top: 468px; width: 442px; height: 277px;
    background: var(--panel);
  }
  .intro-card p {
    position: absolute; left: 38px; top: 64px; width: 318px;
    font-size: 13.2px; line-height: 23.3px; color: var(--white);
  }
  .more-btn {
    position: absolute; left: 40px; top: 232px; width: 147px; height: 38px;
    border: 1px solid rgba(255,255,255,0.7); color: var(--white); text-decoration: none;
    font-size: 10px; font-weight: 500; letter-spacing: 0.5px; text-transform: uppercase;
    display: flex; align-items: center; justify-content: center;
  }

  .feature-photo {
    position: absolute; left: 573px; top: 422px; width: 442px; height: 310px;
    background:
      radial-gradient(ellipse at 60% 75%, var(--photo-vest) 0%, rgba(230,73,43,0) 45%),
      linear-gradient(120deg, var(--photo-warm) 0%, #d9a55a 35%, var(--photo-cool) 80%, #9aa9b8 100%);
    box-shadow: 0 18px 40px rgba(0,0,0,0.18);
  }
  .feature-photo .frame {
    position: absolute; left: 22px; top: 22px; right: 25px; bottom: 23px;
    border: 1px solid rgba(255,255,255,0.85);
  }
</style>
</head>
<body>
<div class="site">
  <section class="hero">
    <span class="grid-line" style="left:793px"></span>
    <span class="grid-line" style="left:1053px"></span>
    <span class="grid-line main" style="left:405px"></span>

    <div class="brand">Halden Constructions</div>

    <nav class="main-nav">
      <a class="active" href="#" style="left:421px">About us</a>
      <a href="#" style="left:549px">Services</a>
      <a href="#" style="left:679px">Projects</a>
      <a href="#" style="left:809px">Culture</a>
      <a href="#" style="left:938px">Contact</a>
    </nav>

    <a class="social-link" href="#" style="left:1037px" aria-label="Social profile 1"></a>
    <a class="social-link" href="#" style="left:1083px" aria-label="Social profile 2"></a>
    <a class="social-link" href="#" style="left:1130px" aria-label="Social profile 3"></a>

    <h1 class="hero-title">Quality Construction</h1>
    <p class="hero-services">Commercial • Residential • Building Maintenance • Project Managmenet</p>

    <svg class="scroll-cue" width="32" height="32" viewBox="0 0 32 32" aria-label="Scroll down">
      <circle cx="16" cy="16" r="15" fill="none" stroke="#ffffff" stroke-opacity="0.8"/>
      <path d="M12.5 14.5 L16 18 L19.5 14.5" fill="none" stroke="#ffffff" stroke-width="1.4"/>
    </svg>

    <svg class="section-dots" width="10" height="160" viewBox="0 0 10 160" aria-label="Section navigation">
      <line x1="5" y1="5" x2="5" y2="155" stroke="#ffffff" stroke-opacity="0.5"/>
      <circle cx="5" cy="5" r="3.5" fill="#ffffff"/>
      <circle cx="5" cy="42" r="3.5" fill="#2a9be9" stroke="#ffffff"/>
      <circle cx="5" cy="80" r="3.5" fill="#2a90e6" stroke="#ffffff"/>
      <circle cx="5" cy="117" r="3.5" fill="#2d86e3" stroke="#ffffff"/>
      <circle cx="5" cy="155" r="3.5" fill="#2f7de0" stroke="#ffffff"/>
    </svg>
  </section>

  <article class="intro-card">
    <p>Lorem ipsum dolor sit amet, consectetur adipisicing elit, sed do eiusmod tempor incididunt ut labore et dolore magna aliqua. Ut enim ad minim veniam, quis nostrud exercitation ullamco laboris nisi ut aliquip ex ea commodo consequat. Duis aute irure</p>
    <a class="more-btn" href="#">More details</a>
  </article>

  <div class="feature-photo" role="img" aria-label="Site supervisors in hard hats and high-visibility vests on a construction site, seen from behind">
    <div class="frame"></div>
  </div>
</div>
</body>
</html>
```